Brochure Projecct

I need a brochure created for my company, which will be sent to customers via email in PDF format. I have uploaded the company logo with this project, which I want incorporated in the design.

Designers should view the company website at www.brightcounselpages.com. I want the brochure to compliment the website (i.e., very clean design). I would also like pictures added to the brochure to make the design visually stunning.

In terms of content, I need four pages in the brochure to add four separate sections of content (one section per page). The four sections of content will be as follows (1) Search Engine Optimization Benefits (2) Increased Client Retention (3) Showcase Your Law Firm (4) Maximize Your Online ROI (5) Pricing Plans. I will give the content to the winning designer to add to the project. Each individual content section will have four subsection titles after which content of approximately 100 to 200 words will appear.

Designers can decide if other pages should be added to the brochure (i.e., a "cover page" that would have little content, but be visually appealing like the cover of a book - - - a "back page" that may just have the logo, contact information, etc).

My company address and email address should be prominently featured through every page (address: 2715 West Juniper Avenue, Suite 1400, Scottsdale, Arizona 85317; email: sales@brightcounselpages.com).

Industry/Entity Type

It Company

Requirements
Must have
• Clean look but visually stunning incorporating the design of the website at brightcounselpages.com as well as the logo. Also, room for content as set forth in the description of this project.

```html
<!DOCTYPE html>
<html lang="en">
<head>
<meta charset="utf-8">
<title>Bright Counsel Pages – Newsletter Brochure</title>
<link rel="stylesheet" href="https://fonts.googleapis.com/css2?family=Mulish:wght@300;400;600;700;800&display=swap">
<style>
:root{
  --blue:#1f86c8;
  --blue-light:#4aa7de;
  --blue-pale:#8cc6ea;
  --ink:#2a2a2c;
  --dark:#38383b;
  --gray:#8d8e91;
  --gray-mid:#a9aaad;
  --gray-light:#c9cacc;
  --paper:#ffffff;
  --stage:#eceeef;
  --text-on-dark:#c4c5c8;
  --body-text:#6a6b6e;
}
*{box-sizing:border-box;margin:0;padding:0}
html,body{width:1200px;height:1200px;overflow:hidden}
body{
  font-family:"Mulish",sans-serif;
  background:radial-gradient(circle at 50% 45%,#f7f8f8 0%,var(--stage) 70%);
  position:relative;color:var(--ink);
}
.page{
  position:absolute;width:280px;height:396px;background:var(--paper);overflow:hidden;
  box-shadow:0 3px 8px rgba(0,0,0,.22);
}
.page--dark{background:var(--dark)}
.page-title{position:absolute;left:14px;top:16px;font-size:9.5px;font-weight:800;color:var(--ink);white-space:nowrap}
.page-rule{position:absolute;left:14px;right:14px;top:32px;height:.6px;background:var(--gray-light)}
.page-num{position:absolute;right:14px;top:10px;font-size:4px;color:var(--gray)}
.sections{position:absolute;left:14px;top:42px;width:252px}
.sub{font-size:7.5px;font-weight:300;color:var(--blue-light);margin-bottom:3px;white-space:nowrap}
.body{font-size:4px;line-height:5.6px;color:var(--body-text);margin-bottom:10px;text-align:justify}
.body--narrow{width:86px}
.photo{
  position:absolute;border:3px solid #fff;box-shadow:0 1px 4px rgba(0,0,0,.35);
  background:linear-gradient(150deg,#5a4236 0%,#b8896d 45%,#e8c3a8 70%,#6b5244 100%);
}
.footer{position:absolute;left:0;bottom:0;width:280px;height:90px}
.footer svg.band{position:absolute;inset:0;width:100%;height:100%}
.contact{position:absolute;left:10px;top:50px;font-size:3.4px;line-height:4.4px;color:var(--text-on-dark)}
.contact--light{color:#555}
.contact-row{display:flex;gap:6px;align-items:flex-start;margin-bottom:3px}
.contact-row svg{width:8px;height:8px;flex:none}
.contact-web{color:var(--blue-light);font-size:5.5px;line-height:8px}
.brand{position:absolute;right:12px;bottom:18px;display:flex;align-items:center;gap:3px;font-size:5px;font-weight:700;color:#fff}
.brand--light{color:var(--ink)}
.brand-dot{width:10px;height:10px;border-radius:50%;background:var(--blue)}
.sidebar{position:absolute;left:0;top:0;width:85px;height:330px;background:var(--dark)}
.side-num{position:absolute;left:12px;top:10px;font-size:4px;color:var(--text-on-dark)}
.side-label{position:absolute;left:12px;font-size:6.5px;font-weight:300;color:var(--text-on-dark);white-space:nowrap}
.page-title--blue{color:var(--blue);left:95px;font-size:8.5px}
.col{position:absolute;left:95px;top:42px;width:172px}
.split{display:flex;gap:14px;align-items:flex-start;margin-bottom:10px}
.split .body{margin-bottom:0;flex:none}
.quote{position:relative;font-size:7px;line-height:8px;font-weight:300;color:var(--blue-light);padding-left:2px}
.quote::before{content:"\201C";font-size:16px;position:absolute;left:-9px;top:1px;color:var(--blue-light)}
.quote--dark{color:#d8d9db;text-align:center}
.thumbs{position:absolute;display:flex;gap:8px}
.thumb{width:18px;height:18px;border:1.5px solid #fff;box-shadow:0 1px 2px rgba(0,0,0,.35);
  background:linear-gradient(150deg,#5a4236,#c99b7d 55%,#6b5244)}
.page--dark .sub{color:var(--text-on-dark)}
.page--dark .body{color:#a5a6a9}
.cover{position:absolute;left:61px;top:524px;width:431px;height:608px;background:#fff;overflow:hidden;box-shadow:0 3px 10px rgba(0,0,0,.25)}
.cover-brand{position:absolute;right:36px;top:70px;display:flex;align-items:center;gap:8px;font-size:15px;font-weight:700;color:var(--ink)}
.cover-brand .brand-dot{width:26px;height:26px}
.cover-date{position:absolute;left:33px;top:138px;font-size:20px;font-weight:300;color:var(--blue)}
.cover-title{position:absolute;left:33px;top:164px;font-size:28.5px;font-weight:800;color:var(--ink);letter-spacing:-.4px;white-space:nowrap}
.cover-subtitle{position:absolute;left:33px;top:200px;font-size:20px;font-weight:300;color:var(--blue)}
.cover-rule{position:absolute;left:33px;top:236px;width:205px;height:.8px;background:var(--gray-light)}
.issue-head{position:absolute;left:33px;top:248px;font-size:11px;font-weight:300;color:var(--ink);letter-spacing:.3px}
.issue-list{position:absolute;left:37px;top:272px;list-style:none}
.issue-list li{font-size:9px;font-weight:300;color:var(--blue);height:21px}
.issue-list li::before{content:"•";margin-right:8px}
.cover-contact{position:absolute;left:8px;top:455px;font-size:5.5px;line-height:7px;color:var(--text-on-dark)}
.cover-contact .contact-row{gap:14px;margin-bottom:10px;align-items:center}
.cover-contact .contact-row svg{width:15px;height:15px}
.cover-contact .contact-web{font-size:10px;line-height:14px}
</style>
</head>
<body>

<!-- Page: Showcase Your Law Firm -->
<section class="page" style="left:105px;top:82px">
  <h2 class="page-title">Showcase Your Law Firm</h2>
  <span class="page-num">4</span>
  <div class="page-rule"></div>
  <div class="sections">
    <h3 class="sub">Subtitle Section</h3>
    <p class="body">Clear pages help local clients find your firm, learn what you offer and reach out with confidence. Each section below explains one simple step that brings steady visits, stronger trust and more calls to your office every month. Clear pages help local clients find your firm, learn what you offer and reach out with confidence. Each section below explains one simple step that brings steady visits, stronger trust and more calls to your office every month.</p>
    <h3 class="sub">Subtitle Section</h3>
    <p class="body">Clear pages help local clients find your firm, learn what you offer and reach out with confidence. Each section below explains one simple step that brings steady visits, stronger trust and more calls to your office every month. Clear pages help local clients find your firm, learn what you offer and reach out with confidence. Each section below explains one simple step that brings steady visits, stronger trust and more calls to your office every month.</p>
    <h3 class="sub">Subtitle Section</h3>
    <p class="body">Clear pages help local clients find your firm, learn what you offer and reach out with confidence. Each section below explains one simple step that brings steady visits, stronger trust and more calls to your office every month. Clear pages help local clients find your firm, learn what you offer and reach out with confidence. Each section below explains one simple step that brings steady visits, stronger trust and more calls to your office every month.</p>
    <h3 class="sub">Subtitle Section</h3>
    <p class="body body--narrow">Short notes on results, reviews and profile updates keep your listing fresh. Short notes on results, reviews and profile updates keep your listing fresh.</p>
  </div>
  <div class="photo" role="img" aria-label="Portrait photo of a smiling professional woman" style="left:158px;top:210px;width:92px;height:74px"></div>
  <div class="photo" role="img" aria-label="Portrait photo of a smiling young woman" style="left:104px;top:258px;width:94px;height:84px;transform:rotate(-14deg)"></div>
  <div class="footer">
    <svg class="band" viewBox="0 0 280 90" preserveAspectRatio="none" aria-hidden="true">
      <path d="M0 34 C90 24 190 14 280 4 L280 28 C190 32 90 38 0 46 Z" fill="var(--blue)"/>
      <path d="M0 46 C90 38 190 32 280 28 L280 90 L0 90 Z" fill="var(--dark)"/>
    </svg>
    <div class="contact">
      <div class="contact-row"><svg viewBox="0 0 16 16"><path d="M8 1 1 7.5h2V15h4v-4h2v4h4V7.5h2Z" fill="#fff"/></svg><span>2715 West Juniper Avenue<br>Suite 1400<br>Scottsdale<br>Arizona 85317</span></div>
      <div class="contact-row"><svg viewBox="0 0 16 16"><rect x="1" y="3" width="14" height="10" fill="#fff"/><path d="M1 3l7 6 7-6" fill="none" stroke="var(--dark)" stroke-width="1.3"/></svg><span>sales@brightcounselpages.com</span></div>
      <div class="contact-row"><svg viewBox="0 0 16 16"><circle cx="8" cy="8" r="6.5" fill="none" stroke="#fff" stroke-width="1.5"/><path d="M1.5 8h13M8 1.5c-3 3.5-3 9.5 0 13M8 1.5c3 3.5 3 9.5 0 13" fill="none" stroke="#fff" stroke-width="1.1"/></svg><span class="contact-web">www.brightcounselpages.com</span></div>
    </div>
    <div class="brand"><span class="brand-dot"></span>Bright Counsel Pages</div>
  </div>
</section>

<!-- Page: Maximize Your Online ROI -->
<section class="page" style="left:471px;top:82px">
  <div class="sidebar">
    <span class="side-num">5</span>
    <span class="side-label" style="top:42px">Subtitle Section</span>
    <span class="side-label" style="top:92px">Subtitle Section</span>
    <span class="side-label" style="top:142px">Subtitle Section</span>
    <span class="side-label" style="top:212px">Subtitle Section</span>
  </div>
  <h2 class="page-title page-title--blue">Maximize Your Online ROI</h2>
  <div class="page-rule" style="left:95px"></div>
  <div class="col">
    <p class="body">Clear pages help local clients find your firm, learn what you offer and reach out with confidence. Each section below explains one simple step that brings steady visits, stronger trust and more calls to your office every month. Clear pages help local clients find your firm, learn what you offer and reach out with confidence. Each section below explains one simple step that brings steady visits, stronger trust and more calls to your office every month.</p>
    <p class="body">Clear pages help local clients find your firm, learn what you offer and reach out with confidence. Each section below explains one simple step that brings steady visits, stronger trust and more calls to your office every month. Clear pages help local clients find your firm, learn what you offer and reach out with confidence. Each section below explains one simple step that brings steady visits, stronger trust and more calls to your office every month.</p>
    <div class="split">
      <p class="body" style="width:50px">Short notes on results, reviews and profile updates keep your listing fresh.</p>
      <blockquote class="quote" style="width:104px">Proin hendrerit egestas bibendum. Suspendisse mollis nunc mollis. Sed nec mi risus. Integer nec justo lorem. Quisque quis elit, purus, a elementum leo.</blockquote>
    </div>
    <p class="body">Clear pages help local clients find your firm, learn what you offer and reach out with confidence. Each section below explains one simple step that brings steady visits, stronger trust and more calls to your office every month. Clear pages help local clients find your firm, learn what you offer and reach out with confidence. Each section below explains one simple step that brings steady visits, stronger trust and more calls to your office every month.</p>
  </div>
  <div class="thumbs" style="left:130px;top:276px">
    <div class="thumb" role="img" aria-label="Small portrait photo" style="transform:rotate(-8deg)"></div>
    <div class="thumb" role="img" aria-label="Small portrait photo"></div>
    <div class="thumb" role="img" aria-label="Small portrait photo" style="transform:rotate(6deg)"></div>
    <div class="thumb" role="img" aria-label="Small portrait photo"></div>
  </div>
  <div class="footer">
    <svg class="band" viewBox="0 0 280 90" preserveAspectRatio="none" aria-hidden="true">
      <path d="M0 34 C90 24 190 14 280 4 L280 28 C190 32 90 38 0 46 Z" fill="var(--blue)"/>
      <path d="M0 46 C90 38 190 32 280 28 L280 90 L0 90 Z" fill="var(--dark)"/>
    </svg>
    <div class="contact">
      <div class="contact-row"><svg viewBox="0 0 16 16"><path d="M8 1 1 7.5h2V15h4v-4h2v4h4V7.5h2Z" fill="#fff"/></svg><span>2715 West Juniper Avenue<br>Suite 1400<br>Scottsdale<br>Arizona 85317</span></div>
      <div class="contact-row"><svg viewBox="0 0 16 16"><rect x="1" y="3" width="14" height="10" fill="#fff"/><path d="M1 3l7 6 7-6" fill="none" stroke="var(--dark)" stroke-width="1.3"/></svg><span>sales@brightcounselpages.com</span></div>
      <div class="contact-row"><svg viewBox="0 0 16 16"><circle cx="8" cy="8" r="6.5" fill="none" stroke="#fff" stroke-width="1.5"/><path d="M1.5 8h13M8 1.5c-3 3.5-3 9.5 0 13M8 1.5c3 3.5 3 9.5 0 13" fill="none" stroke="#fff" stroke-width="1.1"/></svg><span class="contact-web">www.brightcounselpages.com</span></div>
    </div>
    <div class="brand"><span class="brand-dot"></span>Bright Counsel Pages</div>
  </div>
</section>

<!-- Page: Pricing Plans -->
<section class="page" style="left:837px;top:82px">
  <h2 class="page-title">Pricing Plans</h2>
  <span class="page-num">6</span>
  <div class="page-rule"></div>
  <div class="sections">
    <h3 class="sub">Subtitle Section</h3>
    <p class="body">Clear pages help local clients find your firm, learn what you offer and reach out with confidence. Each section below explains one simple step that brings steady visits, stronger trust and more calls to your office every month. Clear pages help local clients find your firm, learn what you offer and reach out with confidence. Each section below explains one simple step that brings steady visits, stronger trust and more calls to your office every month.</p>
    <h3 class="sub">Subtitle Section</h3>
    <p class="body">Clear pages help local clients find your firm, learn what you offer and reach out with confidence. Each section below explains one simple step that brings steady visits, stronger trust and more calls to your office every month. Clear pages help local clients find your firm, learn what you offer and reach out with confidence. Each section below explains one simple step that brings steady visits, stronger trust and more calls to your office every month.</p>
    <h3 class="sub">Subtitle Section</h3>
    <p class="body">Clear pages help local clients find your firm, learn what you offer and reach out with confidence. Each section below explains one simple step that brings steady visits, stronger trust and more calls to your office every month. Clear pages help local clients find your firm, learn what you offer and reach out with confidence. Each section below explains one simple step that brings steady visits, stronger trust and more calls to your office every month.</p>
    <h3 class="sub">Subtitle Section</h3>
    <p class="body body--narrow">Short notes on results, reviews and profile updates keep your listing fresh. Short notes on results, reviews and profile updates keep your listing fresh.</p>
  </div>
  <div class="photo" role="img" aria-label="Portrait photo of a smiling professional woman" style="left:158px;top:210px;width:92px;height:74px"></div>
  <div class="photo" role="img" aria-label="Portrait photo of a smiling young woman" style="left:104px;top:258px;width:94px;height:84px;transform:rotate(-14deg)"></div>
  <div class="footer">
    <svg class="band" viewBox="0 0 280 90" preserveAspectRatio="none" aria-hidden="true">
      <path d="M0 34 C90 24 190 14 280 4 L280 28 C190 32 90 38 0 46 Z" fill="var(--blue)"/>
      <path d="M0 46 C90 38 190 32 280 28 L280 90 L0 90 Z" fill="var(--dark)"/>
    </svg>
    <div class="contact">
      <div class="contact-row"><svg viewBox="0 0 16 16"><path d="M8 1 1 7.5h2V15h4v-4h2v4h4V7.5h2Z" fill="#fff"/></svg><span>2715 West Juniper Avenue<br>Suite 1400<br>Scottsdale<br>Arizona 85317</span></div>
      <div class="contact-row"><svg viewBox="0 0 16 16"><rect x="1" y="3" width="14" height="10" fill="#fff"/><path d="M1 3l7 6 7-6" fill="none" stroke="var(--dark)" stroke-width="1.3"/></svg><span>sales@brightcounselpages.com</span></div>
      <div class="contact-row"><svg viewBox="0 0 16 16"><circle cx="8" cy="8" r="6.5" fill="none" stroke="#fff" stroke-width="1.5"/><path d="M1.5 8h13M8 1.5c-3 3.5-3 9.5 0 13M8 1.5c3 3.5 3 9.5 0 13" fill="none" stroke="#fff" stroke-width="1.1"/></svg><span class="contact-web">www.brightcounselpages.com</span></div>
    </div>
    <div class="brand"><span class="brand-dot"></span>Bright Counsel Pages</div>
  </div>
</section>

<!-- Cover -->
<section class="cover">
  <svg style="position:absolute;left:0;top:0" width="120" height="90" viewBox="0 0 120 90" aria-hidden="true">
    <circle cx="10" cy="-10" r="95" fill="var(--gray-mid)"/>
    <circle cx="0" cy="-20" r="80" fill="var(--blue-pale)"/>
  </svg>
  <svg style="position:absolute;left:318px;top:240px" width="113" height="130" viewBox="0 0 113 130" aria-hidden="true">
    <circle cx="85" cy="65" r="65" fill="var(--gray-mid)"/>
    <circle cx="95" cy="60" r="48" fill="var(--blue-pale)"/>
  </svg>
  <div class="cover-brand"><span class="brand-dot"></span>Bright Counsel Pages</div>
  <p class="cover-date">April 2013</p>
  <h1 class="cover-title">Title of the Newsletter</h1>
  <p class="cover-subtitle">Subtitle</p>
  <div class="cover-rule"></div>
  <p class="issue-head">IN THIS ISSUE:</p>
  <ul class="issue-list">
    <li>Search Engine Optimization Benefits</li>
    <li>Increased Client Retention</li>
    <li>Showcase Your Law Firm</li>
    <li>Maximize Your Online ROI</li>
    <li>Pricing Plans</li>
  </ul>
  <svg style="position:absolute;left:0;bottom:0" width="431" height="250" viewBox="0 0 431 250" preserveAspectRatio="none" aria-hidden="true">
    <path d="M0 18 C140 10 300 4 431 0 L431 26 C300 30 140 36 0 44 Z" fill="var(--blue)"/>
    <path d="M0 44 C140 36 300 30 431 26 L431 250 L0 250 Z" fill="var(--dark)"/>
  </svg>
  <div class="cover-contact">
    <div class="contact-row"><svg viewBox="0 0 16 16"><path d="M8 1 1 7.5h2V15h4v-4h2v4h4V7.5h2Z" fill="#fff"/></svg><span>2715 West Juniper Avenue<br>Suite 1400<br>Scottsdale<br>Arizona 85317</span></div>
    <div class="contact-row"><svg viewBox="0 0 16 16"><rect x="1" y="3" width="14" height="10" fill="#fff"/><path d="M1 3l7 6 7-6" fill="none" stroke="var(--dark)" stroke-width="1.3"/></svg><span>sales@brightcounselpages.com</span></div>
    <div class="contact-row"><svg viewBox="0 0 16 16"><circle cx="8" cy="8" r="6.5" fill="none" stroke="#fff" stroke-width="1.5"/><path d="M1.5 8h13M8 1.5c-3 3.5-3 9.5 0 13M8 1.5c3 3.5 3 9.5 0 13" fill="none" stroke="#fff" stroke-width="1.1"/></svg><span class="contact-web">www.brightcounselpages.com</span></div>
  </div>
</section>

<!-- Page: Search Engine Optimization Benefits -->
<section class="page page--dark" style="left:525px;top:630px">
  <h2 class="page-title" style="color:var(--blue);font-size:8.5px">Search Engine Optimization Benefits</h2>
  <span class="page-num">2</span>
  <div class="page-rule" style="background:var(--blue)"></div>
  <div class="sections">
    <h3 class="sub">Subtitle Section</h3>
    <div class="split">
      <p class="body" style="width:150px">Clear pages help local clients find your firm, learn what you offer and reach out with confidence. Each section below explains one simple step that brings steady visits, stronger trust and more calls to your office every month. Clear pages help local clients find your firm, learn what you offer and reach out with confidence. Each section below explains one simple step that brings steady visits, stronger trust and more calls to your office every month.</p>
      <blockquote class="quote quote--dark" style="width:86px;margin-top:-8px">Proin hendrerit egestas bibendum. Suspendisse mollis nunc mollis. Sed nec mi risus. Integer nec justo lorem. Quisque quis elit, purus, a elementum leo.</blockquote>
    </div>
    <h3 class="sub">Subtitle Section</h3>
    <p class="body">Clear pages help local clients find your firm, learn what you offer and reach out with confidence. Each section below explains one simple step that brings steady visits, stronger trust and more calls to your office every month. Clear pages help local clients find your firm, learn what you offer and reach out with confidence. Each section below explains one simple step that brings steady visits, stronger trust and more calls to your office every month.</p>
    <h3 class="sub">Subtitle Section</h3>
    <p class="body">Clear pages help local clients find your firm, learn what you offer and reach out with confidence. Each section below explains one simple step that brings steady visits, stronger trust and more calls to your office every month. Clear pages help local clients find your firm, learn what you offer and reach out with confidence. Each section below explains one simple step that brings steady visits, stronger trust and more calls to your office every month.</p>
    <h3 class="sub">Subtitle Section</h3>
    <p class="body">Clear pages help local clients find your firm, learn what you offer and reach out with confidence. Each section below explains one simple step that brings steady visits, stronger trust and more calls to your office every month. Clear pages help local clients find your firm, learn what you offer and reach out with confidence. Each section below explains one simple step that brings steady visits, stronger trust and more calls to your office every month.</p>
  </div>
  <div class="footer">
    <svg class="band" viewBox="0 0 280 90" preserveAspectRatio="none" aria-hidden="true">
      <path d="M0 0 L280 0 L280 4 C190 14 90 24 0 34 Z" fill="var(--dark)"/>
      <path d="M0 34 C90 24 190 14 280 4 L280 28 C190 32 90 38 0 46 Z" fill="var(--blue)"/>
      <path d="M0 46 C90 38 190 32 280 28 L280 90 L0 90 Z" fill="#ffffff"/>
    </svg>
    <div class="contact contact--light">
      <div class="contact-row"><svg viewBox="0 0 16 16"><path d="M8 1 1 7.5h2V15h4v-4h2v4h4V7.5h2Z" fill="var(--dark)"/></svg><span>2715 West Juniper Avenue<br>Suite 1400<br>Scottsdale<br>Arizona 85317</span></div>
      <div class="contact-row"><svg viewBox="0 0 16 16"><rect x="1" y="3" width="14" height="10" fill="var(--dark)"/><path d="M1 3l7 6 7-6" fill="none" stroke="#fff" stroke-width="1.3"/></svg><span>sales@brightcounselpages.com</span></div>
      <div class="contact-row"><svg viewBox="0 0 16 16"><circle cx="8" cy="8" r="6.5" fill="none" stroke="var(--dark)" stroke-width="1.5"/><path d="M1.5 8h13M8 1.5c-3 3.5-3 9.5 0 13M8 1.5c3 3.5 3 9.5 0 13" fill="none" stroke="var(--dark)" stroke-width="1.1"/></svg><span class="contact-web" style="color:var(--blue)">www.brightcounselpages.com</span></div>
    </div>
    <div class="brand brand--light"><span class="brand-dot"></span>Bright Counsel Pages</div>
  </div>
</section>

<!-- Page: Increased Client Retention -->
<section class="page" style="left:837px;top:630px">
  <div class="sidebar">
    <span class="side-num">3</span>
    <span class="side-label" style="top:44px">Subtitle Section</span>
    <span class="side-label" style="top:92px">Subtitle Section</span>
    <span class="side-label" style="top:140px">Subtitle Section</span>
    <span class="side-label" style="top:188px">Subtitle Section</span>
    <span class="side-label" style="top:236px">Subtitle Section</span>
  </div>
  <h2 class="page-title page-title--blue">Increased Client Retention</h2>
  <div class="page-rule" style="left:95px"></div>
  <div class="col">
    <p class="body" style="margin-bottom:7px">Clear pages help local clients find your firm, learn what you offer and reach out with confidence. Each section below explains one simple step that brings steady visits, stronger trust and more calls to your office every month. Clear pages help local clients find your firm, learn what you offer and reach out with confidence. Each section below explains one simple step that brings steady visits, stronger trust and more calls to your office every month.</p>
    <p class="body" style="margin-bottom:7px">Clear pages help local clients find your firm, learn what you offer and reach out with confidence. Each section below explains one simple step that brings steady visits, stronger trust and more calls to your office every month. Clear pages help local clients find your firm, learn what you offer and reach out with confidence. Each section below explains one simple step that brings steady visits, stronger trust and more calls to your office every month.</p>
    <p class="body" style="margin-bottom:7px">Clear pages help local clients find your firm, learn what you offer and reach out with confidence. Each section below explains one simple step that brings steady visits, stronger trust and more calls to your office every month. Clear pages help local clients find your firm, learn what you offer and reach out with confidence. Each section below explains one simple step that brings steady visits, stronger trust and more calls to your office every month.</p>
    <p class="body" style="margin-bottom:7px">Clear pages help local clients find your firm, learn what you offer and reach out with confidence. Each section below explains one simple step that brings steady visits, stronger trust and more calls to your office every month. Clear pages help local clients find your firm, learn what you offer and reach out with confidence. Each section below explains one simple step that brings steady visits, stronger trust and more calls to your office every month.</p>
    <p class="body" style="margin-bottom:7px">Clear pages help local clients find your firm, learn what you offer and reach out with confidence. Each section below explains one simple step that brings steady visits, stronger trust and more calls to your office every month. Clear pages help local clients find your firm, learn what you offer and reach out with confidence. Each section below explains one simple step that brings steady visits, stronger trust and more calls to your office every month.</p>
  </div>
  <div class="footer">
    <svg class="band" viewBox="0 0 280 90" preserveAspectRatio="none" aria-hidden="true">
      <path d="M0 34 C90 24 190 14 280 4 L280 28 C190 32 90 38 0 46 Z" fill="var(--blue)"/>
      <path d="M0 46 C90 38 190 32 280 28 L280 90 L0 90 Z" fill="#ffffff"/>
    </svg>
    <div class="contact contact--light">
      <div class="contact-row"><svg viewBox="0 0 16 16"><path d="M8 1 1 7.5h2V15h4v-4h2v4h4V7.5h2Z" fill="var(--dark)"/></svg><span>2715 West Juniper Avenue<br>Suite 1400<br>Scottsdale<br>Arizona 85317</span></div>
      <div class="contact-row"><svg viewBox="0 0 16 16"><rect x="1" y="3" width="14" height="10" fill="var(--dark)"/><path d="M1 3l7 6 7-6" fill="none" stroke="#fff" stroke-width="1.3"/></svg><span>sales@brightcounselpages.com</span></div>
      <div class="contact-row"><svg viewBox="0 0 16 16"><circle cx="8" cy="8" r="6.5" fill="none" stroke="var(--dark)" stroke-width="1.5"/><path d="M1.5 8h13M8 1.5c-3 3.5-3 9.5 0 13M8 1.5c3 3.5 3 9.5 0 13" fill="none" stroke="var(--dark)" stroke-width="1.1"/></svg><span class="contact-web" style="color:var(--blue)">www.brightcounselpages.com</span></div>
    </div>
    <div class="brand brand--light"><span class="brand-dot"></span>Bright Counsel Pages</div>
  </div>
</section>

</body>
</html>
```